Innovative WordPress for a non-profit organization dedicated to providing healthcare to the less for

Bright Harbor Relief is a small non-profit organization. BHR's core mission is to provide free medical and dental care to the less fortunate. Aside from providing healthcare, BHR also helps build infrastructure such as orphanage, cancer centers, water wells and small homes for the homeless. As a non-profit, BHR has been sponsoring various social programs to help those in need. From building infrastructure to health care and most recently micro-finance, the BHR team is helping to GIve Back to the community at person at a time.

BHR is growing and needs help to restructure for the future. The corporate website design is the first step in a new branding strategy for the company.

BHR current website is divided into three specific target areas:
1. Mission: This area is dedicated to provide information about medical and dental mission hosted by BHR.

2. Infrastructure. This area is dedicated to provide information about infrastructure programs supported and completed by the BHR team. The projects includes orphanage, cancer centers. water wells, micro-finance, small homes for the homeless...etc.

3. Special Projects. This area is used to showcase specific short term projects which might come up.

Aside from the specific three target area, BHR also needs a NEWS area where news about BHR can be published.

Please put your thinking cape on and help produce the next generation WordPress template for Bright Harbor Relief. Your design will great enhance the level of volunteers recruited and also increase the level of help that BHR can provide for other.

For a quick glance at the BHR website today, please visit http://www.brightharborrelief-example.org. The BHR team is looking for a fresh design.

Thank you very much for taking the time to help BHR advance its mission of helping those in need.

Reason: Seeking more variety in design. Design needs to have a donate button, sponsors area, news, welcome message, 3 primary functions (mission, infrastructure, and specials projects). The BHR logo is available. Please note, you have the option to NOT use the colors associated with BHR logo. Thank you for helping with designing the new site.

Non-Profit

Must have
• 1. Donate Now button.
2. Primary focus areas: MISSION / INFRASTRUCTURE / SPECIAL PROJECTS
3. News & Events
4. Welcome Message area
5. Sponsors area - place to add sponsor logos

Nice to have
• 1. Photo of the Month: Used to show a specific photo to represent events or functions completed by the BHR team.

Please show sample of one level down. For example, what does the page look like when I click the MISSION link.

```html
<!DOCTYPE html>
<html lang="en">
<head>
<meta charset="utf-8">
<title>Bright Harbor Relief</title>
<link rel="stylesheet" href="https://fonts.googleapis.com/css2?family=Open+Sans:wght@400;600;700&display=swap">
<style>
:root{
  --ink:#1c1c1c;
  --bar:#1b1b1b;
  --paper:#f1f0ec;
  --muted:#8a8a8a;
  --text:#333;
  --red:#e31b23;
  --green:#1f9a3d;
  --yellow:#f4d21c;
  --orange:#f39a0c;
  --orange-dark:#e27d05;
  --gold:#f2c02a;
  --link:#2a6fc9;
  --sponsor:#3a3a3a;
}
*{box-sizing:border-box;margin:0;padding:0}
html,body{width:1080px;height:1200px;overflow:hidden}
body{background:var(--paper);font-family:'Open Sans',Arial,sans-serif;color:var(--text);position:relative}
.abs{position:absolute}

/* top bar */
.topbar{left:0;top:0;width:1080px;height:22px;background:var(--bar);color:#fff}
.topbar .tagline{left:460px;top:4px;font-size:11px;font-weight:700;letter-spacing:.3px}
.topbar .icon{top:4px}
.topbar .social-label{left:766px;top:5px;font-size:9px;font-weight:600}
.topbar .sq{top:4px;width:14px;height:14px;border-radius:2px}
.topbar .donate-btn{left:850px;top:3px;width:48px;height:16px;border:1px solid #777;background:#2b2b2b;font-size:9px;text-align:center;line-height:14px;letter-spacing:.3px}

/* header */
.brand{left:180px;top:40px;width:110px}
.brand .name{font-size:28px;font-weight:700;color:var(--ink);line-height:30px}
.brand .sub{font-size:6.5px;font-weight:700;color:var(--ink);letter-spacing:.2px}
.nav a{position:absolute;top:49px;font-size:10px;color:#999;text-decoration:none;letter-spacing:.2px}
.nav a.active{color:var(--ink)}

/* hero */
.hero{left:0;top:86px;width:1080px;height:459px;background:linear-gradient(100deg,#5e4a3c 0%,#d8cfc6 22%,#3a5fa8 40%,#7c8fc2 55%,#2a2622 70%,#a86c7a 85%,#3b2f2f 100%)}
.hero-caption{left:586px;top:86px;width:316px;height:94px;background:rgba(0,0,0,.72);color:#fff;text-align:right;padding:8px 16px 0 10px}
.hero-caption h2{font-size:15px;font-weight:600;line-height:18px}
.hero-caption p{font-size:10.5px;line-height:15px;margin-top:2px}
.welcome{left:180px;top:388px;width:300px;background:rgba(0,0,0,.72);color:#fff;padding:8px 12px}
.welcome h2{font-size:13px;font-weight:600;line-height:16px}
.welcome p{font-size:9.5px;line-height:13px;margin-top:3px}
.thumbstrip{left:0;top:468px;width:1080px;height:77px;background:rgba(15,15,15,.78)}
.thumb{top:481px;width:114px;height:52px;background:linear-gradient(135deg,#6a5b52,#c7c3c0 50%,#3d6d3c);border:1px solid #444}
.arrow{top:501px}

/* focus areas */
.focus{top:562px;width:156px;height:72px;border:1px solid #dcdad4;background:#f6f5f1}
.focus h3{height:27px;line-height:27px;text-align:center;color:#fff;font-size:16px;font-weight:400;letter-spacing:.3px}
.focus p{font-size:8.5px;line-height:11px;text-align:center;color:#666;padding:5px 6px}
.focus.mission h3{background:var(--green)}
.focus.infra h3{background:var(--yellow)}
.focus.special h3{background:var(--red)}

/* donation */
.raise{left:714px;top:562px;width:188px;height:168px;background:linear-gradient(#f7b21b,var(--orange-dark));border:1px solid #e49a0c}
.raise h3{color:#fff;font-size:14.5px;font-weight:700;text-align:center;margin-top:6px;letter-spacing:.2px}
.counter{display:flex;gap:2px;justify-content:center;margin-top:8px}
.counter span{width:14px;height:20px;background:#fff;color:#222;font-size:13px;font-weight:600;text-align:center;line-height:20px;border-radius:2px}
.progress{margin:9px auto 0;width:164px;height:10px;background:#fff;border-radius:5px;overflow:hidden}
.progress i{display:block;width:36%;height:100%;background:var(--gold)}
.amounts{display:grid;grid-template-columns:repeat(3,36px);gap:6px 14px;justify-content:center;margin-top:8px}
.amounts span{height:15px;background:linear-gradient(#ffcd3c,#f19a06);border:1px solid #c77605;color:#fff;font-size:8px;font-weight:700;text-align:center;line-height:13px}
.donate-now{display:block;margin:8px auto 0;width:116px;height:22px;background:var(--red);border:1px solid #fff;color:#fff;font-size:13px;text-align:center;line-height:20px}

/* feature news */
.section-title{color:var(--red);font-size:20px;font-weight:600}
.news-item{left:180px;width:246px}
.news-item h4{font-size:10.5px;font-weight:600;color:var(--ink);line-height:13px}
.news-item p{font-size:8.5px;color:var(--muted);line-height:17px;margin-top:6px}
.read-more{left:340px;width:86px;height:26px;background:var(--ink);color:#fff;font-size:11px;text-align:center;line-height:26px;border-radius:2px}
.photo{background:linear-gradient(120deg,#c49a5a,#f3ede5 45%,#d8c5ac 70%,#9c7d54)}

/* latest news */
.latest{left:714px;top:746px}
.latest p{font-size:8.5px;color:#444;margin-top:1px}
.email{left:714px;top:787px;width:134px;height:18px;background:#fff;border:1px solid #ccc;font-size:8px;color:#bbb;padding:3px 5px}
.go{left:858px;top:787px;width:44px;height:18px;background:var(--ink);color:#fff;font-size:10px;text-align:center;line-height:18px}

/* events */
.events{left:714px;top:826px;width:188px;height:280px;background:#ddd}
.events h3{height:34px;background:linear-gradient(#3a3a3a,#111);color:var(--gold);font-size:18px;font-weight:700;padding:4px 8px}
.event{display:flex;height:73px;border-bottom:1px solid #cfcfcf;background:#e4e4e4}
.event .date{width:50px;display:flex;align-items:center;justify-content:center;font-size:10px;font-weight:700;color:var(--ink);background:#e9e9e9}
.event .date.hot{color:var(--red)}
.event .body{flex:1;padding:6px 6px 0 6px;background:#d6d6d6}
.event h5{font-size:9px;font-weight:700;color:var(--ink);line-height:11px}
.event p{font-size:7.5px;color:#777;line-height:10px;margin-top:3px}
.event p a{color:var(--link);text-decoration:underline}
.view-all{display:block;height:26px;background:linear-gradient(#2c2c2c,#000);color:#fff;font-size:13px;text-align:center;line-height:26px;margin-top:2px}

/* cards */
.card{top:948px;width:164px;text-align:center}
.card .photo{height:86px;border:2px solid var(--yellow)}
.card h4{color:var(--red);font-size:10.5px;font-weight:400;margin-top:7px;letter-spacing:.3px}
.card p{text-align:left;font-size:8.5px;color:#555;line-height:11px;margin-top:3px;padding-left:2px}
.card .more{display:inline-block;margin-top:13px;width:70px;height:22px;background:var(--red);color:#fff;font-size:8px;font-weight:700;line-height:22px}

/* footer */
.footer{left:0;top:1140px;width:1080px;height:60px;background:var(--bar);color:#fff;text-align:center}
.footer nav{margin-top:14px;font-size:8.5px;letter-spacing:.2px}
.footer nav span{margin:0 4px;color:#aaa}
.footer .rights{font-size:8px;font-weight:700;margin-top:6px}
.sponsors{left:180px;top:12px;display:flex;align-items:center;gap:6px}
.sponsors .label{font-size:8px;font-weight:700;color:#ccc;letter-spacing:.3px;margin-right:4px}
.sponsors i{display:block;width:26px;height:26px;background:var(--sponsor);border-radius:3px}
</style>
</head>
<body>

<header>
  <div class="topbar abs">
    <div class="tagline abs">SERVING THE DISADVANTAGE COMMUNITY</div>
    <svg class="icon abs" style="left:708px" width="14" height="14" viewBox="0 0 14 14" aria-label="RSS feed"><circle cx="3" cy="11" r="1.6" fill="#fff"/><path d="M2 6a6 6 0 0 1 6 6M2 2a10 10 0 0 1 10 10" stroke="#fff" stroke-width="1.8" fill="none"/></svg>
    <svg class="icon abs" style="left:732px" width="15" height="14" viewBox="0 0 15 14" aria-label="Email"><rect x="1" y="3" width="13" height="9" fill="#fff"/><path d="M1 3l6.5 5L14 3" stroke="#1b1b1b" fill="none"/></svg>
    <div class="social-label abs">Social</div>
    <div class="sq abs" style="left:796px;background:#3fa9e0" aria-label="Social link"></div>
    <div class="sq abs" style="left:814px;background:#3b5998" aria-label="Social link"></div>
    <div class="donate-btn abs">DONATE</div>
  </div>

  <div class="brand abs">
    <div class="name">BHR</div>
    <div class="sub">BRIGHT HARBOR RELIEF</div>
  </div>

  <nav class="nav">
    <a class="active" style="left:410px">HOME</a>
    <a style="left:476px">ABOUT US</a>
    <a style="left:558px">MISSION</a>
    <a style="left:634px">SPECIAL PROJECTS</a>
    <a style="left:752px">INFRASTRUCTURE</a>
    <a style="left:866px">EVENTS</a>
  </nav>
</header>

<section>
  <div class="hero abs" role="img" aria-label="Photo of two volunteers smiling beside a dental clinic sponsor board"></div>
  <div class="hero-caption abs">
    <h2>DR. MINH CARVER &amp; LENA PARK<br>VOLUNTEERING AT A DENTAL CLINIC.</h2>
    <p>Dr. Minh Carver and Lena Park volunteering at the BHR Dental Clinic hosted at Riverside Community Hall, Lakeview, VA on May 17, 2014.</p>
  </div>
  <div class="welcome abs">
    <h2>WELCOME TO BRIGHT HARBOR RELIEF</h2>
    <p>Free medical and dental care, and homes, wells and hope for those in need.</p>
  </div>
  <div class="thumbstrip abs"></div>
  <svg class="arrow abs" style="left:178px" width="12" height="14" viewBox="0 0 12 14" aria-label="Previous"><path d="M10 1L2 7l8 6z" fill="#666"/></svg>
  <div class="thumb abs" style="left:204px" role="img" aria-label="Thumbnail photo of volunteers"></div>
  <div class="thumb abs" style="left:344px" role="img" aria-label="Thumbnail photo of volunteer group"></div>
  <div class="thumb abs" style="left:484px" role="img" aria-label="Thumbnail photo of dental treatment"></div>
  <div class="thumb abs" style="left:623px" role="img" aria-label="Thumbnail photo of volunteers"></div>
  <div class="thumb abs" style="left:762px" role="img" aria-label="Thumbnail photo of clinic room"></div>
  <svg class="arrow abs" style="left:890px" width="12" height="14" viewBox="0 0 12 14" aria-label="Next"><path d="M2 1l8 6-8 6z" fill="#666"/></svg>
</section>

<section>
  <div class="focus mission abs" style="left:180px"><h3>MISSION</h3><p>This area is dedicated to provide information about medical and dental mission hosted by BHR.</p></div>
  <div class="focus infra abs" style="left:358px"><h3>INFRASTRUCTURE</h3><p>This area is dedicated to provide information about infrastructure programs supported and…</p></div>
  <div class="focus special abs" style="left:538px"><h3>SPECIAL PROJECTS</h3><p>This area is used to showcase specific short term projects which might come up</p></div>

  <div class="raise abs">
    <h3>YOU'VE HELPED RAISE...</h3>
    <div class="counter"><span>$</span><span>0</span><span>0</span><span>1</span><span>5</span><span>5</span><span>3</span><span>1</span></div>
    <div class="progress"><i></i></div>
    <div class="amounts"><span>$ 1</span><span>$ 5</span><span>$ 10</span><span>$ 20</span><span>$ 50</span><span>Other</span></div>
    <span class="donate-now">DONATE NOW</span>
  </div>
</section>

<section>
  <h2 class="section-title abs" style="left:180px;top:658px">FEATURE NEWS</h2>
  <div class="news-item abs" style="top:688px">
    <h4>DR. CLARA WYNN (FAR RIGHT) WORKING WITH THE VOLUNTEERS AT A BHR DENTAL CLINIC.</h4>
    <p>Dr. Clara Wynn mentoring a group of volunteers who will be future dentist at the BHR Dental Clinic.</p>
  </div>
  <div class="read-more abs" style="top:755px">READ MORE</div>
  <div class="photo abs" style="left:451px;top:666px;width:242px;height:115px" role="img" aria-label="Photo of dental volunteers in white coats"></div>

  <div class="news-item abs" style="top:825px">
    <h4>DR. CLARA WYNN (FAR RIGHT) WORKING WITH THE VOLUNTEERS AT A BHR DENTAL CLINIC.</h4>
    <p>Dr. Clara Wynn mentoring a group of volunteers who will be future dentist at the BHR Dental Clinic.</p>
  </div>
  <div class="read-more abs" style="top:893px">READ MORE</div>
  <div class="photo abs" style="left:451px;top:803px;width:242px;height:115px" role="img" aria-label="Photo of dental volunteers in white coats"></div>

  <div class="latest abs">
    <h2 class="section-title">LATEST NEWS</h2>
    <p>Events, stories, giveaways and upcoming events</p>
  </div>
  <div class="email abs">Email</div>
  <div class="go abs">&gt;&gt; GO</div>

  <div class="events abs">
    <h3>EVENTS</h3>
    <div class="event"><div class="date hot">Jan-28</div><div class="body"><h5>LOREM IPSUM DOLOR SIT AM ET, CONSECTE</h5><p>Adipiscing elit. Etiam sed sodales neque. Nulla vel risus vitae orci pharetra rhoncu <a>Read more</a></p></div></div>
    <div class="event"><div class="date">Jan-28</div><div class="body"><h5>LOREM IPSUM DOLOR SIT AM ET, CONSECTE</h5><p>Adipiscing elit. Etiam sed sodales neque. Nulla vel risus vitae orci pharetra rhoncu <a>Read more</a></p></div></div>
    <div class="event"><div class="date">Jan-28</div><div class="body"><h5>LOREM IPSUM DOLOR SIT AM ET, CONSECTE</h5><p>Adipiscing elit. Etiam sed sodales neque. Nulla vel risus vitae orci pharetra rhoncu <a>Read more</a></p></div></div>
    <span class="view-all">VIEW ALL</span>
  </div>
</section>

<section>
  <div class="card abs" style="left:180px">
    <div class="photo" role="img" aria-label="Photo of dental volunteers"></div>
    <h4>ETIAM SUSCIPIT FEUGIAT</h4>
    <p>Lorem ipsum dolor sit amet, consectetur adipiscing elit. Maecenas tristique turpis nec orci bibendum, a luctus risus</p>
    <span class="more">› More Details</span>
  </div>
  <div class="card abs" style="left:356px">
    <div class="photo" role="img" aria-label="Photo of a dental treatment session"></div>
    <h4>ETIAM SUSCIPIT FEUGIAT</h4>
    <p>Lorem ipsum dolor sit amet, consectetur adipiscing elit. Maecenas tristique turpis nec orci bibendum, a luctus risus</p>
    <span class="more">› More Details</span>
  </div>
  <div class="card abs" style="left:532px">
    <div class="photo" role="img" aria-label="Photo of clinic staff with a patient"></div>
    <h4>ETIAM SUSCIPIT FEUGIAT</h4>
    <p>Lorem ipsum dolor sit amet, consectetur adipiscing elit. Maecenas tristique turpis nec orci bibendum, a luctus risus</p>
    <span class="more">More Details</span>
  </div>
</section>

<footer class="footer abs">
  <div class="sponsors abs" aria-label="Sponsors">
    <span class="label">SPONSORS</span><i></i><i></i><i></i><i></i>
  </div>
  <nav>HOME<span>|</span>ABOUT US<span>|</span>MISSION<span>|</span>SPECIAL PROJECTS<span>|</span>INFRASTRUCTURE<span>|</span>EVENTS</nav>
  <div class="rights">ALL RIGHTS RESERVED</div>
</footer>

</body>
</html>
```